11 x 17 Thelanoros Quote

Design the following quote in a poster.

"First say to yourself what you would be; then do what you have to do." - Thelanoros

See here for inspiration - https://prints.quietgrove.com/

Quote

```html
<!DOCTYPE html>
<html lang="en">
<head>
<meta charset="UTF-8">
<title>Thelanoros Quote Poster</title>
<link href="https://fonts.googleapis.com/css2?family=Oswald:wght@400;500;600&family=Playfair+Display:ital,wght@1,700&display=swap" rel="stylesheet">
<style>
  :root {
    --backdrop: #3a3a3a;
    --poster-border: #ffffff;
    --poster-paper: #d9d9d9;
    --paper-shade: #c9c9c9;
    --bubble: #bcbcbc;
    --ink: #4b4b4b;
    --ink-strong: #111111;
    --badge: #3f3f3f;
    --badge-mark: #ffffff;
  }
  * { margin: 0; padding: 0; box-sizing: border-box; }
  html, body {
    width: 1200px;
    height: 899px;
    overflow: hidden;
    background: var(--backdrop);
  }
  .poster {
    position: absolute;
    left: 293px;
    top: 21px;
    width: 614px;
    height: 857px;
    background: var(--poster-border);
    padding: 18px;
  }
  .poster-paper {
    position: relative;
    width: 100%;
    height: 100%;
    background: radial-gradient(ellipse at 40% 35%, var(--poster-paper) 0%, var(--paper-shade) 100%);
    overflow: hidden;
  }
  .speech-bubble {
    position: absolute;
    left: 0;
    top: 0;
    width: 578px;
    height: 821px;
  }
  .quote-badge {
    position: absolute;
    left: 233px;
    top: 28px;
    width: 112px;
    height: 112px;
  }
  .quote-text {
    position: absolute;
    left: 34px;
    top: 160px;
    width: 510px;
    font-family: "Oswald", sans-serif;
    font-weight: 500;
    font-size: 68px;
    line-height: 74px;
    text-align: center;
    text-transform: uppercase;
    color: var(--ink);
    letter-spacing: 0.5px;
  }
  .quote-text .emphasis {
    color: var(--ink-strong);
    font-weight: 600;
  }
  .quote-author {
    position: absolute;
    left: 0;
    top: 752px;
    width: 100%;
    text-align: center;
    font-family: "Playfair Display", serif;
    font-style: italic;
    font-weight: 700;
    font-size: 22px;
    color: var(--ink);
  }
</style>
</head>
<body>
  <main class="poster">
    <div class="poster-paper">
      <svg class="speech-bubble" viewBox="0 0 578 821" aria-hidden="true">
        <path d="M60 84 H518 a26 26 0 0 1 26 26 V687 a26 26 0 0 1 -26 26 H308 L289 735 L270 713 H60 a26 26 0 0 1 -26 -26 V110 a26 26 0 0 1 26 -26 Z" fill="var(--bubble)"/>
      </svg>
      <svg class="quote-badge" viewBox="0 0 112 112" aria-hidden="true">
        <circle cx="56" cy="56" r="56" fill="var(--badge)"/>
        <circle cx="39" cy="64" r="13" fill="var(--badge-mark)"/>
        <path d="M27 62 C27 46 36 37 49 34 L50 40 C41 43 37 50 37 58 Z" fill="var(--badge-mark)"/>
        <circle cx="73" cy="64" r="13" fill="var(--badge-mark)"/>
        <path d="M61 62 C61 46 70 37 83 34 L84 40 C75 43 71 50 71 58 Z" fill="var(--badge-mark)"/>
      </svg>
      <p class="quote-text">
        “First say to<br>
        <span class="emphasis">yourself</span><br>
        what you<br>
        would be;<br>
        then do<br>
        what you<br>
        have to do.”
      </p>
      <p class="quote-author">– Thelanoros</p>
    </div>
  </main>
</body>
</html>
```